Lucia Verena a furniture, interior design and home decor Brand

I need complete stationary for a new brand, business card, postcard, letter head, shipping envelopes, tissue paper, etc... I would like to use copper foil on some of these items. I have a logo design. I would like to see

Target Market(s)

Furniture,Interior Design & Home Decor

Industry/Entity Type

Interior Design

Colors
606060
7f7f7f

Requirements
Must have
• My signature style is spanish medeterrenean, my brand colors is charcoal gray with copper. Would love to see a wrought iron panel illustration created, I have attahced a few samples of wrought iron illustration I am attracted to, also an example of packing that has the pattern in foil.
Should not have
• Will not be using the word Design, only Lucia Verena and LV icon

```html
<!DOCTYPE html>
<html lang="en">
<head>
<meta charset="utf-8">
<title>Lucia Verena – Business Card</title>
<link rel="stylesheet" href="https://fonts.googleapis.com/css2?family=Jost:wght@400;500;600&display=swap">
<style>
  :root {
    --backdrop: #2a2a2a;
    --card-white: #ffffff;
    --charcoal: #575757;
    --copper: #d8693a;
    --copper-deep: #cf5b26;
    --copper-light: #f7ae84;
    --ink-light: #ffffff;
  }
  * { margin: 0; padding: 0; box-sizing: border-box; }
  html, body {
    width: 1125px;
    height: 1200px;
    overflow: hidden;
    background: var(--backdrop);
    font-family: "Jost", "Futura", sans-serif;
  }
  .card {
    position: absolute;
    left: 150px;
    width: 825px;
    height: 471px;
    border-radius: 26px;
    overflow: hidden;
  }
  .card--front { top: 98px; background: var(--card-white); }
  .card--back { top: 631px; height: 470px; background: var(--charcoal); }

  .wave { position: absolute; inset: 0; width: 100%; height: 100%; }

  .brand {
    position: absolute;
    display: flex;
    align-items: center;
    gap: 22px;
  }
  .brand__mark {
    width: 110px;
    height: 110px;
    border: 2px solid var(--copper);
    border-radius: 50%;
  }
  .brand__name {
    color: var(--copper);
    font-weight: 400;
    font-size: 36px;
    letter-spacing: 0.5px;
    white-space: nowrap;
  }
  .card--front .brand { left: 60px; top: 67px; }

  .contact {
    position: absolute;
    right: 46px;
    color: var(--ink-light);
    text-align: right;
  }
  .contact__name { top: 216px; font-size: 29px; font-weight: 600; line-height: 1.1; right: 46px; }
  .contact__role { top: 253px; font-size: 19px; font-weight: 600; right: 46px; }

  .contact-list {
    position: absolute;
    right: 46px;
    top: 304px;
    list-style: none;
    color: var(--ink-light);
  }
  .contact-list li {
    display: flex;
    justify-content: flex-end;
    align-items: center;
    gap: 10px;
    height: 26.5px;
    font-size: 19px;
  }
  .contact-list svg { width: 18px; height: 18px; fill: var(--ink-light); }
  .contact__address { top: 411px; font-size: 19px; }

  .back-ring { position: absolute; left: 25px; top: 21px; width: 430px; height: 430px; }
  .card--back .brand { left: 492px; top: 330px; }
  .card--back .brand__name { font-size: 40px; }
</style>
</head>
<body>

<section class="card card--front">
  <svg class="wave" viewBox="0 0 800 456" preserveAspectRatio="none" aria-hidden="true">
    <defs>
      <linearGradient id="band-upper" x1="0" y1="0" x2="1" y2="0">
        <stop offset="0" stop-color="#f7b58f"/>
        <stop offset="0.5" stop-color="#e98656"/>
        <stop offset="1" stop-color="#d4612d"/>
      </linearGradient>
      <radialGradient id="band-lower" cx="0.5" cy="0.75" r="0.6">
        <stop offset="0" stop-color="#f8b387"/>
        <stop offset="0.55" stop-color="#ea8a5a"/>
        <stop offset="1" stop-color="#d45e29"/>
      </radialGradient>
    </defs>
    <path d="M0,360 C170,392 300,392 430,290 C570,180 680,140 800,148 L800,456 L0,456 Z" fill="url(#band-upper)"/>
    <path d="M0,388 C180,428 310,398 440,300 C580,196 690,150 800,152 L800,456 L0,456 Z" fill="#ffffff"/>
    <path d="M0,393 C180,433 312,402 443,304 C583,200 692,155 800,157 L800,456 L0,456 Z" fill="url(#band-lower)"/>
  </svg>

  <div class="brand">
    <span class="brand__mark" aria-hidden="true"></span>
    <span class="brand__name">Lucia Verena</span>
  </div>

  <p class="contact contact__name">Lucia Verena</p>
  <p class="contact contact__role">CEO/Founder</p>

  <ul class="contact-list">
    <li>555 214 7730
      <svg viewBox="0 0 24 24" aria-hidden="true"><path d="M6.6 10.8a15.1 15.1 0 0 0 6.6 6.6l2.2-2.2a1 1 0 0 1 1-.25 11.4 11.4 0 0 0 3.6.57 1 1 0 0 1 1 1V20a1 1 0 0 1-1 1A17 17 0 0 1 3 4a1 1 0 0 1 1-1h3.5a1 1 0 0 1 1 1c0 1.25.2 2.45.57 3.6a1 1 0 0 1-.25 1z"/></svg>
    </li>
    <li>555 382 1946
      <svg viewBox="0 0 24 24" aria-hidden="true"><path d="M7 1h10a2 2 0 0 1 2 2v18a2 2 0 0 1-2 2H7a2 2 0 0 1-2-2V3a2 2 0 0 1 2-2zm0 3v15h10V4z"/></svg>
    </li>
    <li>hello@luciaverena.com
      <svg viewBox="0 0 24 24" aria-hidden="true"><path d="M2 5h20v14H2zm2 2v.5l8 5 8-5V7l-8 5z"/></svg>
    </li>
    <li>www.luciaverena.com
      <svg viewBox="0 0 24 24" aria-hidden="true"><path d="M12 2a10 10 0 1 0 0 20 10 10 0 0 0 0-20zm-1 17.9A8 8 0 0 1 4.1 10L9 15v1a2 2 0 0 0 2 2zm6.9-2.5A2 2 0 0 0 16 16h-1v-3a1 1 0 0 0-1-1H8v-2h2a1 1 0 0 0 1-1V7h2a2 2 0 0 0 2-2v-.4a8 8 0 0 1 2.9 12.8z"/></svg>
    </li>
  </ul>

  <p class="contact contact__address">412 Olive Court, Santa Rosa, California 95401</p>
</section>

<section class="card card--back">
  <svg class="back-ring" viewBox="0 0 430 430" aria-hidden="true">
    <defs>
      <linearGradient id="ring-copper" x1="0" y1="0" x2="1" y2="1">
        <stop offset="0" stop-color="#f2a57a"/>
        <stop offset="0.5" stop-color="#d8693a"/>
        <stop offset="1" stop-color="#f0a076"/>
      </linearGradient>
    </defs>
    <circle cx="215" cy="215" r="212" fill="none" stroke="url(#ring-copper)" stroke-width="3"/>
  </svg>
  <div class="brand">
    <span class="brand__name">Lucia Verena</span>
  </div>
</section>

</body>
</html>
```